BFCM Creatives Theme

We are looking for an initial design for our BFCM campaign this year to set the theme for all other creatives for BFCM. We are an ecommerce brand selling Merino wool baby clothing. Our flagship product is the Cozyloft Infant Nap Pouch (see images).

We are starting with the request for an instagram post, announcing the sale (details below). This post should be 1080x1350 but also look appealing in the square grid. I've attached a basic brand card showing color palette, fonts, and logos. I will also attach some image options. We are looking for your creativity to shine while aligning with our branding and connecting with the customer. If you have a specific idea and are looking for a specific image please contact us.

Sale Details:
- 20% Off Sitewide
- 11.28.24 - 12.02.24
- Excluding giftcards and imperfects. No rainchecks.

```html
<!DOCTYPE html>
<html lang="en">
<head>
<meta charset="utf-8">
<title>Fleecely BFCM Sale Post</title>
<link href="https://fonts.googleapis.com/css2?family=Poppins:wght@500;700&family=Caveat:wght@400&display=swap" rel="stylesheet">
<style>
  :root {
    --bg: #d9d9d9;
    --ink: #333335;
    --panel: #e0ddd6;
    --band: #f1f1f1;
    --white: #ffffff;
    --crib: #f3f1ed;
    --sack-light: #ece5d9;
    --sack: #ddd2c1;
    --rug: #cbbfa9;
    --label: #8a8277;
  }
  html, body {
    margin: 0;
    padding: 0;
    width: 1200px;
    height: 1197px;
    overflow: hidden;
    background: var(--bg);
  }
  .stage {
    position: relative;
    width: 1200px;
    height: 1197px;
  }
  .post {
    position: absolute;
    left: 141px;
    top: 24px;
    width: 1080px;
    height: 1350px;
    transform: scale(0.85);
    transform-origin: top left;
    overflow: hidden;
    background: var(--panel);
    font-family: "Poppins", sans-serif;
    color: var(--ink);
  }
  .abs { position: absolute; }
  .hero-photo {
    left: 0; top: 0; width: 637px; height: 1350px;
    background:
      radial-gradient(ellipse 380px 560px at 330px 760px, var(--sack-light) 0%, rgba(236,229,217,0) 75%),
      linear-gradient(180deg, var(--crib) 0%, #ebe7e0 30%, var(--sack-light) 50%, var(--sack) 78%, var(--rug) 100%);
  }
  .photo-label {
    left: 60px; top: 640px; width: 517px;
    text-align: center;
    font-weight: 500; font-size: 22px; letter-spacing: 2px;
    text-transform: uppercase;
    color: var(--label);
  }
  .photo-label small {
    display: block; margin-top: 8px;
    font-size: 18px; letter-spacing: 1px; text-transform: none;
  }
  .info-panel { left: 637px; top: 0; width: 443px; height: 1255px; background: var(--panel); }
  .top-bar { left: 0; top: 0; width: 341px; height: 32px; background: var(--ink); }
  .corner-square { left: 34px; top: 54px; width: 87px; height: 86px; background: var(--ink); }
  .stripe { height: 25px; background: var(--band); }
  .stripe-top-1 { left: 926px; top: 22px; width: 154px; }
  .stripe-top-2 { left: 926px; top: 75px; width: 154px; }
  .stripe-left-1 { left: 0; top: 1009px; width: 154px; background: var(--white); }
  .stripe-left-2 { left: 0; top: 1061px; width: 154px; background: var(--white); }
  .discount {
    left: 674px; top: 172px; margin: 0;
    font-weight: 700; font-size: 188px; line-height: 170px; letter-spacing: -2px;
  }
  .sitewide-band {
    left: 637px; top: 513px; width: 443px; height: 113px; background: var(--band);
    display: flex; align-items: center; justify-content: center;
    font-weight: 700; font-size: 86px; line-height: 1;
  }
  .calendar { left: 816px; top: 657px; width: 68px; height: 70px; }
  .dates {
    left: 637px; top: 740px; width: 443px; text-align: center;
    font-weight: 700; font-size: 45px; line-height: 1.2;
  }
  .terms {
    left: 672px; top: 822px; width: 400px; margin: 0; padding: 0; list-style: none;
    font-family: "Caveat", cursive; font-size: 48px; line-height: 54px;
  }
  .terms li { position: relative; padding-left: 50px; margin-bottom: 20px; }
  .terms li::before {
    content: ""; position: absolute; left: 12px; top: 24px;
    width: 12px; height: 12px; border-radius: 50%; background: var(--ink);
  }
  .brand-band {
    left: 369px; top: 1048px; width: 711px; height: 91px; background: var(--band);
    display: flex; align-items: center; justify-content: center; gap: 16px;
  }
  .brand-dot { width: 46px; height: 46px; border-radius: 50%; border: 3px solid var(--ink); box-sizing: border-box; }
  .brand-name { font-weight: 500; font-size: 54px; line-height: 1; }
  .bottom-bar { left: 532px; top: 1255px; width: 548px; height: 95px; background: var(--ink); }
</style>
</head>
<body>
<div class="stage">
  <div class="post">
    <div class="abs hero-photo" role="img" aria-label="Laughing baby sitting on a woven rug in front of a white crib, wearing a cream merino sleep sack with a sheep print"></div>
    <div class="abs photo-label" aria-hidden="true">Product photo<small>Baby in cream sheep-print sleep sack</small></div>
    <div class="abs info-panel"></div>
    <div class="abs top-bar"></div>
    <div class="abs corner-square"></div>
    <div class="abs stripe stripe-top-1"></div>
    <div class="abs stripe stripe-top-2"></div>
    <div class="abs stripe stripe-left-1"></div>
    <div class="abs stripe stripe-left-2"></div>

    <h1 class="abs discount">20%<br>OFF</h1>
    <div class="abs sitewide-band">Sitewide</div>

    <svg class="abs calendar" viewBox="0 0 70 72" aria-hidden="true">
      <rect x="3" y="9" width="64" height="60" rx="8" fill="none" stroke="#333335" stroke-width="5"/>
      <rect x="3" y="9" width="64" height="14" rx="6" fill="#333335"/>
      <rect x="15" y="1" width="6" height="14" rx="3" fill="#333335"/>
      <rect x="49" y="1" width="6" height="14" rx="3" fill="#333335"/>
      <g fill="#333335">
        <rect x="12" y="30" width="9" height="8"/><rect x="25" y="30" width="9" height="8"/><rect x="38" y="30" width="9" height="8"/><rect x="51" y="30" width="9" height="8"/>
        <rect x="12" y="42" width="9" height="8"/><rect x="25" y="42" width="9" height="8"/><rect x="38" y="42" width="9" height="8"/><rect x="51" y="42" width="9" height="8"/>
        <rect x="12" y="54" width="9" height="8"/><rect x="25" y="54" width="9" height="8"/><rect x="38" y="54" width="9" height="8"/>
      </g>
    </svg>
    <div class="abs dates">11.28.24 - 12.02.24</div>

    <ul class="abs terms">
      <li>Excluding giftcards and imperfects</li>
      <li>No rainchecks</li>
    </ul>

    <div class="abs brand-band">
      <span class="brand-dot"></span>
      <span class="brand-name">Fleecely</span>
    </div>
    <div class="abs bottom-bar"></div>
  </div>
</div>
</body>
</html>
```